Tumbler Cafe - Menu Redesign

What We Want

We're looking for a bold redesign of our current menu. Our current menu is tired and boring and does not accurately reflect our revitalization of the Tumbler Cafe brand. Attachments will be submitted with the campaign for menu items.

Design Guidelines

• Creative use of typography and color. Think Bold, Fun, Loud and uninhibited.
• Fluid, easy to read, layout that emphasizes readability.
• The subtle, demure, look of typographic columns (examples below in resources)
• Creative use of 'wells' for menu item highlights as well as great boarders
• Loud typefaces as long as readability is the focus & emphasis.
• Small illustrations/icons but they must not effect or take the focus from the readability of the menu
• Big, oversized, menu that will look great on recycled paper
• Subtle watermarks/illustrations
• creative use of textures / highlights / section breaks

Menu Requirements

• 9”x12” paper size. Please notify us if your design works better in a different format.
• Oversized, designed for printing on recycled paper.
• Single Page Menu (use lunch on front and breakfast on back)
• Do not use $ or "..." in pricing. Please space all prices equally.
• Simplistic layout that emphasizes readability and logical navigation of menu items.
• Acceptable file types
• Photoshop
• Indesign
• illustrator
• Please contact us before you submit a design if you plan on using something else
• HTML/CSS would be a huge benefit. It's not a must, but it will definitely help you win the award.
• Must retain some of our current color scheme (red/orange/yellow – see attachments/website).

NOTE: Please download ALL attached resources for the project.
Updates

Current web site:  www.tumblercafe-example.com

please read attachment:  tumbler_menu_redesign_request.docx

Lots of good information & examples on menus we like and the design elements featured in the menu.

All,

Thanks for your design submissions!  With all the designs that have be submitted so far, we are confident that our money will be well spent.  I have changed the project to non-refundable.  Please continue working on your designs using the design_request doc that's posted for guidelines/requirements.  I will provide specific feedback to designs as needed.

For your convenience:

Design Guidelines

 

Creativeuse of typography and color.  Think Bold,Fun, Loud and uninhibited.

Fluid,easy to read, layout that emphasizes readability.

Thesubtle, demure, look of typographic columns (examples below in resources)

Creativeuse of 'wells' for menu item highlights as well as great boarders

Loudtypefaces as long as readability is the focus & emphasis.

Smallillustrations/icons but they must not effect or take the focus from thereadability of the menu

Big,oversized, menu that will look great on recycled paper

Subtlewatermarks/illustrations

creativeuse of textures / highlights / section breaks

 

  MenuRequirements

 

9”x12”paper size.  Please notify us if yourdesign works better in a different format.

Oversized,designed for printing on recycled paper.

SinglePage Menu (use lunch on front and breakfast on back)

Donot use $ or "..." in pricing.Please space all prices equally.

Simplisticlayout that emphasizes readability and logical navigation of menu items.

Acceptablefile types

Photoshop

Indesign

illustrator 

Pleasecontact us before you submit a design if you plan on using something else

HTML/CSSwould be a huge benefit.  It's not amust, but it will definitely help you win the award.

Mustretain some of our current color scheme (red/orange/yellow – seeattachments/website). 

 

Do Not Use

 

Skeuomorphismin any way.

Wedo not want any actual pictures of food on the menu (subtle illustrations /icons are great and encouraged).

Typefacesthat are hard to read.

Thanks!

dana

Reason: need to incorporate changes to menu / menu items

Please expect some new copy tonight (USA EST) for the breakfast menu items.  Thanks!

dana

COPY UPDATE:  Please check new menu item listing (revision 3) for updated copy.  Please revisit all menu items as I have grouped, consolidated, and eliminated some items.

Thanks!

dana 

DESIGN UPDATE:  I added an omelette hero/jumbotron design that we'd like to use to display the omelettes on the breakfast menu.  It doesn't have to be exactly like this one, it's just meant to be a guideline.  Please take a look and see if you can fit it in to your design.  Also, the copy has been updated for the breakfast & lunch menus.

Reason: Revised design changes not yet received.

Reason: Designer needs more tine to complete final submission. This will be the last extension. Thanks! dana

Target Market(s)

Women - 60% or more. Mostly professionals. 18-55.
Men - Professionals mostly. Judges, Attorneys, Agents, Ect. Ages 18-55.

Industry/Entity Type

Printing

Colors
f37022
ec1f27
f78f20
faa54b
f04a50
fee18a
faee3e

Requirements
Must have
• see menu requirements in task description.
Nice to have
• Design Ideas We Love

http://www.menugallery-example.com/menucraft/archives/stonegate_inn.php
We like: typefaces, typographic columns & layout, use of butcher-block print, simplicity
We don't like: lack of bold, color lack of textures, lack of general vitality in the brand, no use of icons/illustrations

http://www.menugallery-example.com/menucraft/archives/patty_vault.php
We like: typefaces, bold headers & section breaks, texturized typefaces, use of illustrations, and specifically we love how they did the 'custom creation' menu
We don't like: lack of bold color, lack of subtle texturing, little more use of illustrated icons would be nice

http://www.menugallery-example.com/menucraft/archives/the_rowdy_roost.php
We like: use of bold colors, organization & layout, the section highlights are nice
We don't like: lack of textures, lack subtle illustrations/icons.

http://www.menugallery-example.com/menucraft/archives/wexford_mill.php
We like: use of textures, typefaces, layout & organization, single page menu
We don't like: lack of textures, lack of bold color, lack of icons and menu item hightlights

http://www.menugallery-example.com/menucraft/archives/zibbo_caf.php
We like: use of texturing, typesfaces, layout & organization, creative use of illustrations/icons, bold colors
We don't like: not a huge fan of the bordering; and illustrations take up too much room for single page menu

http://www.menugallery-example.com/menucraft/archives/ved_hjornet_af_torvet.php
We like: creative use of typefaces, organization & layout, cool illustrations, oversized menu, section seperators are cool & unique
We don't like: lack of textures, menu items inside illustrations, typefaces can get hard to read in certain areas
Should not have
• Do Not Use

• Skeuomorphism in any way.
• We do not want any actual pictures of food on the menu (subtle illustrations / icons are great and encouraged).
• Typefaces that are hard to read.

```html
<!DOCTYPE html>
<html lang="en">
<head>
<meta charset="utf-8">
<title>Tumbler Cafe – Lunch Menu</title>
<link rel="stylesheet" href="https://fonts.googleapis.com/css2?family=Rubik+Dirt&family=Fjalla+One&family=Noticia+Text:ital,wght@0,400;0,700;1,400;1,700&display=swap">
<style>
:root{
  --orange:#f78f20;
  --orange-deep:#f37022;
  --orange-light:#faa54b;
  --yellow:#fee18a;
  --yellow-bright:#faee3e;
  --cream:#fdf0b0;
  --red:#ec1f27;
  --red-item:#c4143a;
  --wine:#9c2330;
  --stripe:#b8123c;
  --ink:#2a1f1a;
  --paper:#fbf8f4;
  --pink:#f04a50;
}
*{margin:0;padding:0;box-sizing:border-box}
html,body{width:1000px;height:1200px;overflow:hidden;background:#fff}
.menu{position:relative;width:1000px;height:1200px;overflow:hidden;font-family:"Noticia Text",Georgia,serif;color:var(--ink)}
.col{position:absolute;top:0;height:1200px}
.col-left{left:0;width:340px}
.col-mid{left:348px;width:345px;background:var(--cream)}
.col-right{left:700px;width:300px;background:var(--paper)}
.stripe{position:absolute;top:0;width:7px;height:1200px;
  background:repeating-linear-gradient(180deg,var(--stripe) 0 22px,#e2303f 22px 26px,var(--stripe) 26px 40px)}
.stripe-a{left:341px}.stripe-b{left:693px}

.panel-cold{position:absolute;left:0;top:0;width:340px;height:628px;background:var(--orange);padding:30px 18px 0 28px}
.swirl{position:absolute;left:0;top:0;width:340px;height:628px;
  background:radial-gradient(ellipse 140px 420px at 40px 320px,var(--yellow-bright) 0 55%,transparent 56%),
             radial-gradient(ellipse 200px 480px at 60px 300px,var(--orange-light) 0 60%,transparent 61%)}
.border-dots{position:absolute;left:0;top:628px;width:340px;height:9px;
  background:var(--wine);border-top:3px dotted var(--yellow-bright)}
.panel-wraps{position:absolute;left:0;top:637px;width:340px;height:563px;background:var(--wine);padding:30px 18px 0 28px;color:#fff}

.section-title{font-family:"Rubik Dirt",Impact,sans-serif;font-size:30px;line-height:32px;color:var(--ink);letter-spacing:.5px;position:relative}
.panel-wraps .section-title{color:#fff;font-size:30px}
.intro{font-style:italic;font-size:13.5px;line-height:17px;margin:8px 0 0 14px;position:relative}
.intro b{font-style:normal;font-weight:700}
.bread{font-size:13.5px;line-height:17px;margin:2px 0 0 14px;position:relative}
.bread strong{font-family:"Fjalla One",sans-serif;font-weight:400;font-size:14px}
.items{list-style:none;position:relative;margin-top:14px}
.item{margin-bottom:3px}
.item-name{font-family:"Fjalla One",sans-serif;font-size:15.5px;line-height:19px;color:var(--red-item);margin-left:14px}
.panel-wraps .item-name{color:#fff}
.item-desc{font-size:13.5px;line-height:16px;margin-left:26px}
.panel-wraps .item-desc{color:#fff}
.extra{font-family:"Fjalla One",sans-serif;color:var(--red-item);font-size:15px}

.col-mid .inner{position:absolute;left:0;top:30px;width:345px;padding:0 14px 0 2px}
.brush{position:absolute;background:var(--orange-light);opacity:.35;border-radius:50%}
.brush-a{left:150px;top:690px;width:190px;height:160px}
.brush-b{left:0;top:980px;width:200px;height:100px;opacity:.2}
.burgers{position:absolute;left:2px;top:778px;width:330px}

.col-right .inner{position:absolute;left:0;top:30px;width:300px;padding:0 14px 0 5px}
.patch{position:absolute;background:var(--pink);opacity:.1;border-radius:40% 60% 50% 50%}
.patch-a{left:150px;top:60px;width:160px;height:180px}
.patch-b{left:60px;top:480px;width:230px;height:260px}
.col-right .item-name{margin-left:18px}
.col-right .item-desc{margin-left:30px}
.col-right .item{margin-bottom:2px}
.side-add{font-family:"Fjalla One",sans-serif;font-size:15px;color:var(--red-item);margin-left:18px;line-height:22px}
.side-add span{font-family:"Noticia Text",serif;color:var(--ink);font-size:13.5px}
</style>
</head>
<body>
<main class="menu">

  <section class="col col-left">
    <div class="panel-cold">
      <div class="swirl" role="img" aria-label="Decorative yellow swirl texture"></div>
      <h2 class="section-title">COLD SANDWICHES</h2>
      <p class="intro">Served with bag of Crinkle Chips and a fresh dill pickle spear.</p>
      <p class="bread"><strong>Premium Bread Choices:</strong> Rye, White, Whole Wheat, pumpernickel, or 7-grain</p>
      <p class="bread"><strong>with Bagel or Wrap</strong> .50</p>
      <p class="intro" style="margin-top:4px">We proudly serve Ridgeline Meats &amp; Cheeses</p>
      <ul class="items">
        <li class="item"><h3 class="item-name">B.L.T</h3><p class="item-desc">Ridgeline bacon, lettuce, and tomato 4.95</p></li>
        <li class="item"><h3 class="item-name">Turkey Cranberry Sandwich</h3><p class="item-desc">Ridgeline turkey, provolone, lettuce and cranberry mayo 6.25</p></li>
        <li class="item"><h3 class="item-name">Turkey Club</h3><p class="item-desc">Ridgeline turkey, bacon, fresh tomatoes, lettuce, and mayonnaise&nbsp; 7.50</p></li>
        <li class="item"><h3 class="item-name">Deluxe Sandwich</h3><p class="item-desc">Your choice of Ridgeline ham or turkey, fresh tomatoes, lettuce, and mayonnaise&nbsp; 5.95 &nbsp;<span class="extra">with cheese</span> 6.25</p></li>
        <li class="item"><h3 class="item-name">Chicken Salad Club</h3><p class="item-desc">Ridgeline chicken salad, bacon, fresh tomatoes, lettuce, and mayonnaise&nbsp; 8.50</p></li>
        <li class="item"><h3 class="item-name">Specialty Deluxe Sandwich</h3><p class="item-desc">Your choice of our fresh chicken salad, tuna salad, or egg salad, fresh tomatoes, lettuce, and mayonnaise&nbsp; 6.75</p></li>
      </ul>
    </div>
    <div class="border-dots"></div>
    <div class="panel-wraps">
      <h2 class="section-title">WRAPS</h2>
      <ul class="items" style="margin-top:16px">
        <li class="item"><h3 class="item-name">Venetian Wrap</h3><p class="item-desc">Fresh tuna or chicken salad, specialty romaine blend, hot peppers and our signature herbed oil and vinegar dressing 6.95</p></li>
        <li class="item"><h3 class="item-name">Southwest Chicken Wrap</h3><p class="item-desc">Spicy grilled chicken breast, lettuce, tomato, homemade guacamole and our signature chipotle mayo dressing&nbsp; 8.50</p></li>
        <li class="item"><h3 class="item-name">Thai Chicken Wrap</h3><p class="item-desc">Premium grilled chicken covered in our own spicy thai peanut sauce finished with diced cucumbers 6.95</p></li>
        <li class="item"><h3 class="item-name">Philly Cheese Steak Wrap</h3><p class="item-desc">Premium Ridgeline strip steak, provolone, fresh sauteed peppers, and caramelized onions&nbsp; 6.95</p></li>
        <li class="item"><h3 class="item-name">Portabello Mushroom Wrap</h3><p class="item-desc">Fresh roasted red pepper, grilled caramelized onion, and our Caesar dijon dressing&nbsp; 6.95</p></li>
        <li class="item"><h3 class="item-name">Mango Chicken Wrap</h3><p class="item-desc">Herb marinated grilled chicken and our fresh mango salsa&nbsp; 6.95</p></li>
      </ul>
    </div>
  </section>

  <div class="stripe stripe-a"></div>

  <section class="col col-mid">
    <div class="brush brush-a" role="img" aria-label="Faint orange brush texture"></div>
    <div class="brush brush-b" role="img" aria-label="Faint orange brush texture"></div>
    <div class="inner">
      <h2 class="section-title">SIGNATURE SANDWICHES</h2>
      <p class="intro" style="margin-left:24px">Served with bag of Crinkle Chips and a fresh dill pickle slice. All sandwiches served on a grilled kaiser roll unless otherwise specified.</p>
      <p class="intro" style="margin:14px 0 0 24px"><b style="font-style:italic">Choice of Ridgeline Cheeses:</b><br>American, Provolone, Swiss or Cheddar</p>
      <ul class="items" style="margin-top:16px;margin-left:10px">
        <li class="item"><h3 class="item-name">Grilled Chicken Club</h3><p class="item-desc">Grilled chicken marinated in our own herbal blend, bacon, lettuce, tomato, and mayonnaise on a grilled roll&nbsp; 9.50</p></li>
        <li class="item"><h3 class="item-name">Spicy Chicken Sandwich</h3><p class="item-desc">Freshly marinated chicken breast in our own spicy blend with lettuce, tomato, and mayonnaise on a grilled roll&nbsp; 7.50</p></li>
        <li class="item"><h3 class="item-name">Tumbler Melt</h3><p class="item-desc">Your choice of fresh chicken salad or tuna salad, melted provolone, fresh tomatoes, lettuce, and mayonnaise on a grilled bun&nbsp; 7.50</p></li>
        <li class="item"><h3 class="item-name">Reuben</h3><p class="item-desc">Ridgeline pastrami, Swiss, sauerkraut, and our Russian dressing on rye&nbsp; 6.95</p></li>
        <li class="item"><h3 class="item-name">Tumbler Deluxe Sandwich</h3><p class="item-desc">Your choice of Ridgeline turkey or ham, fresh tomato, provolone and fresh honey mustard dressing&nbsp; 6.95</p></li>
        <li class="item"><h3 class="item-name">Deluxe Grilled Cheese</h3><p class="item-desc">Your choice of Ridgeline cheese grilled to perfection with tomato, onion and spinach&nbsp; 5.50</p><p class="item-desc" style="margin-top:4px"><span class="extra">with Ridgeline bacon</span>&nbsp; 6.50</p></li>
        <li class="item"><h3 class="item-name">Buffalo Chicken Sandwich</h3><p class="item-desc">Freshly marinated chicken chicken breast grilled with our buffalo blue cheese sauce, lettuce, fresh tomato&nbsp; 8.50</p></li>
      </ul>
    </div>
    <div class="burgers">
      <h2 class="section-title">TUMBLER BURGERS</h2>
      <ul class="items" style="margin-top:12px;margin-left:10px">
        <li class="item"><h3 class="item-name">Hamburger</h3><p class="item-desc">6oz hand-formed patty, lettuce, tomato, red onion, mayo on a grilled kaiser roll&nbsp; 5.95&nbsp; <span class="extra">with your choice of cheese</span> 6.50</p></li>
        <li class="item"><h3 class="item-name">Bacon Cheeseburger</h3><p class="item-desc">6oz hand-formed patty, American cheddar, Ridgeline hickory smoked bacon, lettuce, tomato, red onion, mayo on a grilled kaiser roll&nbsp; 7.50</p></li>
        <li class="item"><h3 class="item-name">Salsa Cheddar Burger</h3><p class="item-desc">6oz hand-formed patty, American cheddar, our fresh speciality salsa, lettuce, tomato, red onion, mayo on a grilled kaiser roll&nbsp; 6.75</p></li>
        <li class="item"><h3 class="item-name">Mushroom Cheddar Burger</h3><p class="item-desc">6oz hand-formed patty, American cheddar, fresh mushroom caps, lettuce, tomato, red onion, mayo on a grilled kaiser roll&nbsp; 8</p></li>
      </ul>
    </div>
  </section>

  <div class="stripe stripe-b"></div>

  <section class="col col-right">
    <div class="patch patch-a" role="img" aria-label="Faint pink paper texture"></div>
    <div class="patch patch-b" role="img" aria-label="Faint pink paper texture"></div>
    <div class="inner">
      <h2 class="section-title">SALADS</h2>
      <ul class="items" style="margin-top:8px">
        <li class="item"><h3 class="item-name">The Venetian</h3><p class="item-desc">Homemade chicken or tuna Salad tossed with Romaine lettuce, tomatoes, carrots, onions, hot peppers, mushrooms and Herbed up Oil &amp; Vinegar&nbsp; Small 6.95 / Large 7.95</p></li>
        <li class="item"><h3 class="item-name">C.O.S.</h3><p class="item-desc">Our delicious marinated Chicken, grilled to succulent perfection, served over a big romaine garden salad with our homemade caesar dijon dressing&nbsp; Small 6.95 / Large 7.95</p></li>
        <li class="item"><h3 class="item-name">Chef Salad</h3><p class="item-desc">Ham, Turkey &amp; Cheese over a Romaine Garden Mix with your choice of homemade dressing&nbsp; Small 6.95 / Large 8.95</p></li>
        <li class="item"><h3 class="item-name">The Combo</h3><p class="item-desc">Our Chicken, Tuna, and Egg Salad served over a big romaine garden salad, and our herbed oil and vinaigrette dressing on the side&nbsp; any two (2) 7.95&nbsp; any three (3) 8.95</p></li>
        <li class="item"><h3 class="item-name">Pear Gorgonzola Salad</h3><p class="item-desc">Fresh Pears and Crumbed Gorganzola Cheese over a romaine medley, grilled spicy chicken marinated in our own spicy blend, chopped walnuts, and our fresh herbed oil and vinaigrette dressing&nbsp; Small 6.95 / Large 7.95</p></li>
        <li class="item"><h3 class="item-name">Greek Salad</h3><p class="item-desc">Grilled lemon chicken, feta cheese, greek olives, chopped red onion and our Greek vinaigrette over a Romaine medley&nbsp; Small 6.95 / Large 7.95</p></li>
        <li class="item"><h3 class="item-name">Buffalo Chicken Salad</h3><p class="item-desc">grilled buffalo chicken, romaine medley, monterey jack cheese, tomatoes, croutons and red onion with crumbled blue cheese dressing Small 6.95 / Large 7.95</p></li>
        <li class="item"><h3 class="item-name">Ceasar Salad</h3><p class="item-desc">grilled spicy chicken over a romaine medley and our fresh ceasar dressing small 6.95 / large 7.95</p></li>
        <li class="item"><h3 class="item-name">Spinach Salad</h3><p class="item-desc">chopped hard-boiled egg, bacon bits, red onion, carrots, mushroom and our fresh herbed oil and vinaigrette dressing&nbsp; 6.75&nbsp; <span class="extra">with grilled chicken</span> 8.75</p></li>
        <li class="item"><h3 class="item-name">Southwest Salad</h3><p class="item-desc">fresh romaine medley, tomatoes, mexican corn, crushed torilla chips, monterey jack cheese blend, and sliced avocados topped with our fresh chipotle ranch dressing&nbsp; 7.95</p></li>
      </ul>
      <p class="side-add">with spicy chicken <span>9</span></p>
      <p class="side-add">with spicy skirt steak <span>10</span></p>
    </div>
  </section>

</main>
</body>
</html>
```